Velora Aesthetica

Medical doctor providing aesthetic medicine

* Double sided card
* Logo to be on card
Other details:
* Dr. Mirela Kostvan, BSc, MBChB, CCFP
* #214-215, 27903 83 Ave, Surrey, BC, V2T 4K7
* 604-718-2943
* info@veloraclinic.ca
* www.veloraclinic.ca

Industry/Entity Type

Medical / Health & Beauty

Contact Information for Business Card

see 'Project Description'

Colors
0054AA
0677BA
7BADD7
CADEEF
E8F1F8
FFF300
FFF600
FEFA6F
FFFEC7
FFFEE8

Requirements
Must have
• Modern, high-end design

```html
<!DOCTYPE html>
<html lang="en">
<head>
<meta charset="utf-8">
<title>Velora Aesthetica – Business Card</title>
<link rel="stylesheet" href="https://fonts.googleapis.com/css2?family=Montserrat:wght@300;400;500;600;700&display=swap">
<style>
  :root {
    --backdrop: #737373;
    --navy: #22405f;
    --navy-deep: #1c3653;
    --navy-soft: #2a4c70;
    --ink: #253f5f;
    --gold: #d4ae2b;
    --gold-line: #dcc98a;
    --text-grey: #666666;
    --card-white: #ffffff;
  }
  * { box-sizing: border-box; margin: 0; padding: 0; }
  html, body {
    width: 1200px;
    height: 1000px;
    overflow: hidden;
    background: var(--backdrop);
    font-family: "Montserrat", Arial, sans-serif;
  }
  .canvas {
    position: relative;
    width: 1200px;
    height: 1000px;
  }
  .card {
    position: absolute;
    width: 352px;
    height: 613px;
    border-radius: 18px;
    overflow: hidden;
    box-shadow: 3px 4px 6px rgba(0,0,0,0.35);
  }
  .card-front {
    left: 237px;
    top: 194px;
    background: var(--navy);
  }
  .front-pattern {
    position: absolute;
    inset: 0;
    background:
      linear-gradient(160deg, var(--navy-deep) 0%, var(--navy) 45%, var(--navy-soft) 100%);
  }
  .brand-mark {
    position: absolute;
    left: 50%;
    top: 372px;
    width: 70px;
    height: 70px;
    margin-left: -35px;
    border: 2px solid var(--gold);
    border-radius: 50%;
  }
  .brand-name {
    position: absolute;
    left: 0;
    right: 0;
    top: 456px;
    text-align: center;
    color: var(--card-white);
    font-weight: 500;
    font-size: 19px;
    letter-spacing: 4px;
    text-transform: uppercase;
  }
  .card-back {
    left: 630px;
    top: 193px;
    background: var(--card-white);
  }
  .contact-block {
    position: absolute;
    right: 44px;
    top: 152px;
    text-align: right;
  }
  .doctor-name {
    color: var(--ink);
    font-weight: 600;
    font-size: 18.5px;
    line-height: 24px;
  }
  .credentials {
    color: var(--ink);
    font-weight: 500;
    font-size: 16px;
    line-height: 20px;
  }
  .contact-icons {
    display: flex;
    justify-content: flex-end;
    gap: 6px;
    margin-top: 18px;
  }
  .contact-icons svg { display: block; }
  .contact-lines {
    margin-top: 10px;
    color: var(--text-grey);
    font-weight: 300;
    font-size: 18px;
    line-height: 21px;
  }
  .divider {
    width: 100px;
    height: 1px;
    background: var(--gold-line);
    margin: 28px 0 0 auto;
  }
  .address {
    margin-top: 16px;
    color: var(--text-grey);
    font-weight: 300;
    font-size: 16px;
    line-height: 21px;
  }
</style>
</head>
<body>
<main class="canvas">
  <section class="card card-front">
    <div class="front-pattern" role="img" aria-label="Repeating pattern of faint sunrise-over-water marks on navy"></div>
    <div class="brand-mark"></div>
    <p class="brand-name">Velora Aesthetica</p>
  </section>

  <section class="card card-back">
    <div class="contact-block">
      <p class="doctor-name">Dr. Mirela Kostvan</p>
      <p class="credentials">BSc, MBChB, CCFP</p>

      <div class="contact-icons">
        <svg width="27" height="27" viewBox="0 0 27 27" aria-label="Phone">
          <circle cx="13.5" cy="13.5" r="13.5" fill="var(--gold)"/>
          <path d="M9.5 7.5 l2.2 0 l1 3 l-1.4 1.2 a8 8 0 0 0 3.8 3.8 l1.2 -1.4 l3 1 l0 2.2 a1.5 1.5 0 0 1 -1.6 1.4 A10 10 0 0 1 8 9.1 a1.5 1.5 0 0 1 1.5 -1.6 z" fill="#fff"/>
        </svg>
        <svg width="27" height="27" viewBox="0 0 27 27" aria-label="Email">
          <circle cx="13.5" cy="13.5" r="13.5" fill="var(--gold)"/>
          <rect x="7.5" y="9.5" width="12" height="8.5" fill="#fff"/>
          <path d="M7.5 9.5 l6 4.8 l6 -4.8" fill="none" stroke="var(--gold)" stroke-width="1"/>
        </svg>
        <svg width="27" height="27" viewBox="0 0 27 27" aria-label="Website">
          <circle cx="13.5" cy="13.5" r="13.5" fill="var(--gold)"/>
          <g fill="none" stroke="#fff" stroke-width="1.2">
            <circle cx="13.5" cy="13.5" r="6"/>
            <ellipse cx="13.5" cy="13.5" rx="2.6" ry="6"/>
            <line x1="7.5" y1="13.5" x2="19.5" y2="13.5"/>
            <line x1="8.3" y1="10.5" x2="18.7" y2="10.5"/>
            <line x1="8.3" y1="16.5" x2="18.7" y2="16.5"/>
          </g>
        </svg>
      </div>

      <div class="contact-lines">
        <p>(604) 718 2943</p>
        <p>info@veloraclinic.ca</p>
        <p>www.veloraclinic.ca</p>
      </div>

      <div class="divider"></div>

      <div class="address">
        <p>#214-215, 27903 83 Ave</p>
        <p>Surrey, BC, V2T 4K7</p>
      </div>
    </div>
  </section>
</main>
</body>
</html>
```